Author needs a new book, Kindle and Audiobook cover design

I updated and re-edited a book I wrote 25 years ago but now realize the title and design did not get the job done. I am seeking a book, Kindle and audiobook design that will make me stand out. The final design will pop while being sensitive to the nature of the subject. The title of the book is Hollow Altars. Subtitle: Leaving Cold Pews Behind and Mending a Wounded Heart Along the Road by Delia R. Marwick. I am wanting to get the attention of people who have been damaged by a church relationship that started well but ended badly.
Updates

The book title is: Hollow Altars. The Subtitle is: Leaving Cold Pews Behind and Mending a Wounded Heart Along The Road. The dimension is 6x9 (150 pages) and I am the author: Delia R. Marwick

Target Market(s)

People with a church experience; church leadership. Religious abuse victims.

Industry/Entity Type

Christian

Font styles to use
Serif

Colors

Designer to choose colors to be used in the design.

Requirements
Nice to have
• I am not married to the Serif font if another design works better.

```html
<!DOCTYPE html>
<html lang="en">
<head>
<meta charset="utf-8">
<title>Hollow Altars — Book Cover</title>
<link rel="stylesheet" href="https://fonts.googleapis.com/css2?family=Almendra:wght@400;700&family=Roboto:wght@300;700&display=swap">
<style>
  :root {
    --stage-bg: #ffffff;
    --cover-black: #050607;
    --title-gold: #e6c13a;
    --author-gold: #f0c92c;
    --subtitle-grey: #d8dbe0;
    --glow-white: #f4f8fc;
    --sky-blue: #4a6a8c;
    --ground-grey: #8d939a;
    --ground-dark: #2b2f34;
  }
  * { margin: 0; padding: 0; box-sizing: border-box; }
  html, body {
    width: 1200px;
    height: 857px;
    overflow: hidden;
    background: var(--stage-bg);
  }
  .stage {
    position: relative;
    width: 1200px;
    height: 857px;
  }
  .book-cover {
    position: absolute;
    left: 330px;
    top: 23px;
    width: 540px;
    height: 810px;
    background: var(--cover-black);
    overflow: hidden;
    box-shadow: 0 10px 40px rgba(0,0,0,0.25);
  }
  .cover-art {
    position: absolute;
    left: 0;
    top: 250px;
    width: 540px;
    height: 560px;
    display: block;
  }
  .book-title {
    position: absolute;
    top: 52px;
    left: 0;
    width: 100%;
    text-align: center;
    font-family: "Almendra", serif;
    font-weight: 700;
    font-size: 72px;
    line-height: 1;
    color: var(--title-gold);
    letter-spacing: 1px;
  }
  .book-subtitle {
    position: absolute;
    top: 158px;
    left: 50px;
    right: 50px;
    text-align: center;
    font-family: "Roboto", sans-serif;
    font-weight: 300;
    font-size: 18px;
    line-height: 1.35;
    color: var(--subtitle-grey);
  }
  .book-author {
    position: absolute;
    bottom: 36px;
    left: 0;
    width: 100%;
    text-align: center;
    font-family: "Roboto", sans-serif;
    font-weight: 700;
    font-size: 26px;
    letter-spacing: 3px;
    color: var(--author-gold);
    text-transform: uppercase;
  }
</style>
</head>
<body>
<main class="stage">
  <section class="book-cover">
    <svg class="cover-art" viewBox="0 0 540 560" role="img" aria-label="Photograph of a lone figure walking away across cracked dry earth toward a bright burst of light on the horizon under a dark stormy sky">
      <defs>
        <linearGradient id="sky" x1="0" y1="0" x2="0" y2="1">
          <stop offset="0" stop-color="#050607"/>
          <stop offset="0.35" stop-color="#1a2736"/>
          <stop offset="0.55" stop-color="#4a6a8c"/>
          <stop offset="0.62" stop-color="#8d939a"/>
          <stop offset="1" stop-color="#2b2f34"/>
        </linearGradient>
        <radialGradient id="glow" cx="0.5" cy="0.55" r="0.45">
          <stop offset="0" stop-color="#f4f8fc" stop-opacity="1"/>
          <stop offset="0.35" stop-color="#c9d8e8" stop-opacity="0.7"/>
          <stop offset="1" stop-color="#4a6a8c" stop-opacity="0"/>
        </radialGradient>
      </defs>
      <rect width="540" height="560" fill="url(#sky)"/>
      <ellipse cx="270" cy="300" rx="300" ry="170" fill="url(#glow)"/>
    </svg>
    <h1 class="book-title">Hollow Altars</h1>
    <p class="book-subtitle">Leaving Cold Pews Behind and Mending a<br>Wounded Heart Along the Road</p>
    <p class="book-author">Delia R. Marwick</p>
  </section>
</main>
</body>
</html>
```